BRC Business cards

We are a medium sized property company based in London and require a logo, Business card which reflects a professional company and incorporates our catchy name.

Our statement is (Building for the future) we like colours such as royal blue, greens and light browns but will look at anything.

Contact Information for Business Card

Brookcrest Estates Limited
Unit 4, 15-17 Farrowby Lane
London
SE22 7QN

Web: www.brookcrestestates-example.com

Email: brookcrestltd@mailbox-example.com

Telephone: +44-208-555-0142
Fax: +44-208-555-0187

```html
<!DOCTYPE html>
<html lang="en">
<head>
<meta charset="utf-8">
<title>Brookcrest Estates Limited – Business Card</title>
<link rel="stylesheet" href="https://fonts.googleapis.com/css2?family=Arimo:wght@400;700&display=swap">
<style>
  :root {
    --page: #ffffff;
    --blue-core: #0b5fae;
    --blue-mid: #0f4f9e;
    --blue-edge: #1b3c86;
    --green: #6abf4b;
    --white: #ffffff;
  }
  html, body {
    margin: 0;
    padding: 0;
    width: 1200px;
    height: 695px;
    overflow: hidden;
    background: var(--page);
  }
  .card {
    position: absolute;
    left: 59px;
    top: 0;
    width: 1084px;
    height: 693px;
    background: radial-gradient(ellipse 70% 75% at 50% 50%, var(--blue-core) 0%, var(--blue-mid) 45%, var(--blue-edge) 100%);
    font-family: "Arimo", Arial, sans-serif;
    color: var(--white);
  }
  .brand-name {
    position: absolute;
    left: 124px;
    top: 264px;
    margin: 0;
    font-size: 46px;
    font-weight: 700;
    letter-spacing: 0.5px;
    text-transform: uppercase;
    line-height: 1;
    white-space: nowrap;
  }
  .divider {
    position: absolute;
    left: 0;
    top: 327px;
    width: 100%;
    height: 8px;
    background: var(--green);
  }
  .address {
    position: absolute;
    left: 124px;
    top: 392px;
    margin: 0;
    font-style: normal;
    font-size: 32px;
    line-height: 43px;
  }
  .contacts {
    position: absolute;
    left: 124px;
    top: 486px;
    margin: 0;
    padding: 0;
    list-style: none;
    font-size: 32px;
    line-height: 42.5px;
  }
  .contacts li {
    display: flex;
    white-space: nowrap;
  }
  .contacts .label {
    color: var(--green);
    width: 22px;
  }
  .contacts .sep {
    width: 22px;
    text-align: center;
  }
  .contacts .value {
    padding-left: 4px;
  }
</style>
</head>
<body>
  <section class="card">
    <h1 class="brand-name">Brookcrest Estates Limited</h1>
    <div class="divider"></div>
    <address class="address">
      Brookcrest Estates Limited<br>
      Unit 4, 15-17 Farrowby Lane, London SE22
    </address>
    <ul class="contacts">
      <li><span class="label">W</span><span class="sep">:</span><span class="value">www.brookcrestestates-example.com</span></li>
      <li><span class="label">E</span><span class="sep">:</span><span class="value">brookcrestltd@mailbox-example.com</span></li>
      <li><span class="label">T</span><span class="sep">:</span><span class="value">+44-208-555-0142</span></li>
      <li><span class="label">F</span><span class="sep">:</span><span class="value">+44-208-555-0187</span></li>
    </ul>
  </section>
</body>
</html>
```